Velorami.com - have media you dont own! Velorami the idols - Site Concept

VELORAMI those who ENTERTAIN you, who you LISTEN to, who you IDOLISE, and who you 'BORROW' from... VELORAMI the IDOLS the things that are the STARS... see brief concept at www.velorami-example.com

Looking for site concept, something new, very simple transaction, not generic website. Must also drive mobile app download call to action.

In principle, we dont care how you get your media or watch a TV series or download your favourite song, however, if you are honest and love the song/movie/servies or the star, pay them!
The solution should include anonymous/protected end user interaction and digital certificate/rights management process for end users who have media not paid for to velorami and receive an approved digital certificate from Velorami authorised by the relevant media house proving legal ownership of the digital media item (music, video, TV series/episode, movie etc...)

Basic functions:
Consumer: Mobile and Web
Personal media rights administration
1. Capture core data – Create secure and private Profile account
2. Log owned/borrowed media (media legally owned tagged and media 'borrowed' tagged, decision criteria, pledge or purchase (open to ideas, function to browse PC for media on HDD/Songbarrel or mobile, tag ones to pay for etc, capture CD's owned etc. create digital library filing system?)
3. Pledge payment for media - future payment value linked to market value, I like this, not sure I will keep it forever though, pay less? use once?
4. Purchase rights for media - payment based on market value of related media item. (quidlane, credit card or other?)
5. Media Certificate management - secure and PRIVATE distribution of the certificate (open to options here), approved by media house.

design ideas welcome, modern, fast, simple steps, engaging, with sense of privacy, we wont share data, we will just pay the media houses more! Based in Switzerland, managed by Swiss privacy law. transact with min personal data required.

Reason: The service committed to 50+ designs, most received are form one provider, all off the mark and very basic, not impressed so far, was expecting some real design thought rather than standard templates being rehashed, thats not deisgn? Hope in next days I am impressed?

Target Market(s)

Digital Media Consumer

Industry/Entity Type

Media

Number of Pages Required

5+ page

Font styles to use
Sans Serif

Requirements
Must have
• Must have privacy by design, must have simple and minimal steps taken to log and declare media items and pay, with no risk of exposure. Must have payment process, must have interface to easily load media into site, drag drop, search HDD/mobile etc.
Nice to have
• Digital certificate process and admin interaction of site and with media house, secure and trusted process to provide report and logs of payment for media to specific media house and relevant payments made and tracked.
Should not have
• complex workflows are out, complex payment methods.

```html
<!DOCTYPE html>
<html lang="en">
<head>
<meta charset="utf-8">
<title>Velorami – Site Concept</title>
<link rel="stylesheet" href="https://fonts.googleapis.com/css2?family=Open+Sans:ital,wght@0,400;0,600;0,700;1,400&family=Lora:ital@1&display=swap">
<style>
:root{
  --blue:#3b8fdc;
  --blue-dark:#2a6fb5;
  --ink:#222;
  --muted:#666;
  --dark:#1b1b1b;
  --darker:#111;
  --panel:#2b2b2b;
  --white:#fff;
  --light:#f4f6f8;
}
*{box-sizing:border-box;margin:0;padding:0}
html,body{width:805px;height:1200px;overflow:hidden}
body{font-family:"Open Sans",Arial,sans-serif;color:var(--ink);background:var(--white);position:relative}
.btn{display:inline-block;background:var(--blue);color:var(--white);font-size:8px;font-weight:600;letter-spacing:.5px;text-transform:uppercase;padding:5px 12px;border-radius:2px}
.btn-ghost{background:transparent;border:1px solid #ddd;color:var(--white)}
.btn-outline{background:var(--white);border:1px solid #bbb;color:#333}

/* top strip */
.topbar{position:absolute;top:0;left:0;width:805px;height:22px;background:var(--darker);color:#aaa;font-size:7.5px;display:flex;align-items:center;justify-content:space-between;padding:0 90px;z-index:3}
.topbar span{margin-right:12px}

/* hero */
.hero{position:absolute;top:0;left:0;width:805px;height:312px;background:radial-gradient(ellipse at 62% 45%,#6a6a6a 0%,#3a3a3a 35%,#1a1a1a 75%)}
.nav{position:absolute;top:22px;left:0;width:805px;height:40px;display:flex;align-items:center;justify-content:space-between;padding:0 90px;z-index:3}
.logo{font-size:19px;font-weight:600;color:var(--white);display:flex;align-items:center;gap:7px}
.logo i{width:10px;height:10px;border-radius:50%;background:var(--blue);display:block}
.menu{display:flex;font-size:8px;color:#ddd}
.menu a{padding:13px 8px;color:inherit;text-decoration:none}
.menu a.active{background:var(--blue);color:var(--white)}
.hero-copy{position:absolute;top:148px;left:150px;width:330px;color:var(--white);font-size:10px;line-height:1.5}
.hero-copy .btn{margin-top:14px;background:#111;border:1px solid #555}
.dots{position:absolute;top:292px;left:0;width:805px;display:flex;justify-content:center;gap:5px}
.dots i{width:5px;height:5px;border-radius:50%;background:#888}
.dots i:first-child{background:var(--white)}

/* welcome */
.welcome{position:absolute;top:312px;left:0;width:805px;height:133px;padding:18px 90px}
h2{font-weight:400;font-size:17px}
.welcome h2,.how h2{color:var(--blue)}
.welcome p{font-size:7px;color:var(--muted);line-height:1.55;margin:6px 0 10px;width:620px}
.welcome .btn{margin-right:6px}

/* services */
.services{position:absolute;top:445px;left:0;width:805px;height:240px;background:linear-gradient(180deg,#2e2e2e,#1f1f1f);color:var(--white);padding:14px 90px}
.services > p{font-size:7px;color:#bbb;line-height:1.55;margin:6px 0 14px;width:600px}
.grid{display:grid;grid-template-columns:repeat(3,200px);gap:14px 20px;margin-left:-15px}
.item{display:flex;gap:10px}
.item svg{flex:none}
.item p{font-size:7px;color:#ddd;line-height:1.5}
.item .btn{margin-top:6px;font-size:6.5px;padding:3px 9px;background:#444}

/* how it works */
.how{position:absolute;top:685px;left:0;width:805px;height:175px;padding:22px 90px}
.how blockquote{font-family:"Lora",Georgia,serif;font-style:italic;font-size:10px;color:#555;line-height:1.55;width:240px;margin:8px 0 10px}
.how .art{position:absolute;left:440px;top:20px;width:270px;height:135px;border:1px solid #ddd;background:linear-gradient(135deg,#eef3f8,#d6e3ef)}

/* app */
.app{position:absolute;top:860px;left:0;width:805px;height:172px;background:linear-gradient(135deg,#3f8fd6,#2a72bd 60%,#3a86cf);color:var(--white);padding:14px 90px}
.app p{font-size:7px;color:#dce9f7;line-height:1.5;width:540px;margin:5px 0}
.phones{position:absolute;left:125px;top:58px;width:110px;height:110px;background:linear-gradient(180deg,#1b4f8a,#0f2f55);border-radius:8px}
.badge{position:absolute;top:103px;width:82px;height:28px;border-radius:5px}
.badge.one{left:248px;background:#111}
.badge.two{left:340px;background:#8bc43f}

/* footer */
.footer{position:absolute;top:1032px;left:0;width:805px;height:150px;background:var(--dark);color:var(--white);display:grid;grid-template-columns:230px 170px 200px;padding:18px 90px;gap:10px}
.footer h4{font-size:8px;font-weight:700;letter-spacing:.6px;margin-bottom:10px}
.footer label{display:block;font-size:6.5px;color:#aaa;margin-bottom:2px}
.field{height:13px;background:var(--white);margin-bottom:6px;width:190px}
.footer .btn{width:70px;text-align:center;margin-top:3px}
.footer p{font-size:7px;color:#bbb;line-height:1.7}
.social{display:flex;gap:5px}
.social i{width:14px;height:14px;border-radius:50%;border:1px solid #888;display:block}
.bottom{position:absolute;top:1182px;left:0;width:805px;height:18px;background:#0d2a55;color:#9fb3d0;font-size:6.5px;display:flex;align-items:center;justify-content:space-between;padding:0 90px}
.cards{display:flex;gap:3px}
.cards i{width:20px;height:11px;background:#e9e9e9;border-radius:2px;display:block}
</style>
</head>
<body>

<header>
  <div class="topbar">
    <div><span>+41 00 000 00 00</span><span>hello@velorami-example.com</span></div>
    <div>Login</div>
  </div>
  <div class="nav">
    <div class="logo"><i></i>Velorami</div>
    <nav class="menu">
      <a class="active">Home</a><a>About</a><a>Services</a><a>Certification</a><a>Register</a>
    </nav>
  </div>
</header>

<section class="hero" role="img" aria-label="Dark photograph of a hand holding a smartphone with earphones">
  <div class="hero-copy">
    <p>VELORAMI those who ENTERTAIN you, who you LISTEN to, who you IDOLISE, and who you 'BORROW' from...</p>
    <span class="btn">Learn More</span>
  </div>
  <div class="dots"><i></i><i></i><i></i></div>
</section>

<section class="welcome">
  <h2>Welcome to Velorami</h2>
  <p>Velorami lets you declare the music, films and series you enjoy but never paid for, and settle with the people who made them. Log your library in a few steps, choose to pledge or purchase, and receive a digital certificate approved by the media house. No profiles sold, no data shared, only fair pay for the stars you love. Managed under Swiss privacy law, with the least personal data required.</p>
  <span class="btn">Learn More</span><span class="btn">Sign Up</span>
</section>

<section class="services">
  <h2>Our Services</h2>
  <p>VELORAMI makes it simple to log your media, pay the rights holders and keep proof of legal ownership, all while your identity stays private and protected.</p>
  <p style="margin-top:-10px">Pick a service below to see how each step works.</p>
  <div class="grid">
    <div class="item">
      <svg width="30" height="30" viewBox="0 0 30 30"><circle cx="15" cy="15" r="15" fill="#3b8fdc"/><circle cx="15" cy="12" r="4" fill="#fff"/><path d="M8 22a7 6 0 0 1 14 0z" fill="#fff"/></svg>
      <div><p>Create a secure and private profile account in minutes.</p><span class="btn">More</span></div>
    </div>
    <div class="item">
      <svg width="30" height="30" viewBox="0 0 30 30"><circle cx="15" cy="15" r="15" fill="#3b8fdc"/><path d="M15 8v10M10 13l5-5 5 5M9 21h12" stroke="#fff" stroke-width="2" fill="none"/></svg>
      <div><p>Log owned and borrowed media by drag and drop.</p><span class="btn">More</span></div>
    </div>
    <div class="item">
      <svg width="30" height="30" viewBox="0 0 30 30"><circle cx="15" cy="15" r="15" fill="#3b8fdc"/><path d="M9 15l4 4 8-8" stroke="#fff" stroke-width="2.5" fill="none"/></svg>
      <div><p>Pledge a future payment linked to market value of the item.</p><span class="btn">More</span></div>
    </div>
    <div class="item">
      <svg width="30" height="30" viewBox="0 0 30 30"><circle cx="15" cy="15" r="15" fill="#3b8fdc"/><rect x="8" y="10" width="14" height="10" rx="1.5" fill="#fff"/><rect x="8" y="12" width="14" height="2" fill="#3b8fdc"/></svg>
      <div><p>Purchase rights for media with a simple card payment.</p><span class="btn">More</span></div>
    </div>
    <div class="item">
      <svg width="30" height="30" viewBox="0 0 30 30"><circle cx="15" cy="15" r="15" fill="#3b8fdc"/><rect x="9" y="8" width="12" height="14" fill="#fff"/><path d="M11 12h8M11 15h8M11 18h5" stroke="#3b8fdc"/></svg>
      <div><p>Media certificate management, approved by the media house.</p><span class="btn">More</span></div>
    </div>
    <div class="item">
      <svg width="30" height="30" viewBox="0 0 30 30"><circle cx="15" cy="15" r="15" fill="#3b8fdc"/><rect x="10" y="14" width="10" height="8" fill="#fff"/><path d="M12 14v-3a3 3 0 0 1 6 0v3" stroke="#fff" stroke-width="2" fill="none"/></svg>
      <div><p>Private distribution of your certificates, never shared.</p><span class="btn">More</span></div>
    </div>
  </div>
</section>

<section class="how">
  <h2>How its works</h2>
  <blockquote>Time to show respect, appreciation, honour and 'chances', just VELORAMI</blockquote>
  <span class="btn btn-outline">Learn More</span>
  <div class="art" role="img" aria-label="Illustration of people logging media on a computer screen and receiving a certificate"></div>
</section>

<section class="app">
  <h2>Download the App</h2>
  <p>Take your media rights with you. Log songs and episodes from your phone, pay in a tap and keep certificates safe in your pocket.</p>
  <div class="phones" role="img" aria-label="Two smartphones showing the Velorami app"></div>
  <div class="badge one" aria-label="App store download badge"></div>
  <div class="badge two" aria-label="App store download badge"></div>
</section>

<footer class="footer">
  <div>
    <h4>SIGNUP FOR UPDATES</h4>
    <label>Name</label><div class="field"></div>
    <label>Email</label><div class="field"></div>
    <span class="btn">Sign Up</span>
  </div>
  <div>
    <h4>FIND US</h4>
    <p>Telephone: +41 00 000 00 00<br>E-mail: hello@velorami-example.com</p>
  </div>
  <div>
    <h4>KEEP IN TOUCH</h4>
    <div class="social"><i></i><i></i><i></i><i></i></div>
  </div>
</footer>
<div class="bottom">
  <span>Copyright © Velorami. All rights reserved.</span>
  <div class="cards"><i></i><i></i><i></i><i></i></div>
</div>

</body>
</html>
```